organic collagen powder needs packaging design

We are about to start a company, that sells nutritional supplements online - especially on Brindlecart. For now we are in need of a packaging design for organic collagen powder (Types I, II and III) maybe including also elastin and eventually hyaluronic acid, which is going to be our first product. We are planning on developing organic nutritional supplements of any kind and this is our initial product. Our upscale products must commincate a solid value proposition, the easygoing solution of a real problem, be understandable by users, perform their task as easily and efficiently as possible, and become better and harder to part with the more they are used. To us it is of the utmost importance to produce and sell organic quality products, which are free of any preservatives, chemical fillers, economic extenders or any other unhealthy ingredients. We want our products to come across as high-quality ones (but in no way conservative or unadventurous), vivid, hip, friendly, reliable, modern and healthy. People - men and women alike - should generally be able to unmistakably connect any of our products immediately to our company and to our product line, so the product packaging should be maximally distinctive. Since we will also need further packaging design for further products in the future please consider that the packaging design is scalable for further products/product-line up. We are thinking about defining our products mainly through design as we are not exactly sure yet, if we want to have a brand name for the products. The products are supposed to address men and women, that are looking for healthy nutrition, that are eager to stay fit and in health and that have a modern view and attitude about life. Although our Collagen will not be vegan (the product itself will be of animal origin = hydrolysed bovine collagen), we basically strive for plant based and vegan nutritional supplements without any unnecessary additives.

Target Market(s)

Hip men and women, who want to stay healthy and fit and have an easygoing, modern attitude to life.

Industry/Entity Type

Nutritional supplements, organic (largely vegan products - when possible and reasonable)

Requirements
Must have
• Maximally distinctive design
Nice to have
• Design should be vivid and happy
Should not have
• simple black packaging with simple writing on it

```html
<!DOCTYPE html>
<html lang="en">
<head>
<meta charset="UTF-8">
<title>Organic Collagen Powder – Label</title>
<link rel="stylesheet" href="https://fonts.googleapis.com/css2?family=Josefin+Sans:wght@400;600;700&family=Fira+Sans+Condensed:wght@500;600;700&display=swap">
<style>
  :root{
    --page-bg:#f1f1f3;
    --band-purple:#98289c;
    --band-purple-dark:#7e1f86;
    --ink-navy:#2b2f86;
    --ink-dark:#24243a;
    --wash-lilac:#e6cdf0;
    --wash-pink:#d98fe0;
    --wash-white:#f6f0fa;
    --silver-light:#f4f6f8;
    --silver-mid:#c9ced6;
    --silver-dark:#9aa1ab;
    --white:#ffffff;
  }
  *{margin:0;padding:0;box-sizing:border-box;}
  html,body{width:1200px;height:900px;overflow:hidden;background:var(--page-bg);}
  .label{
    position:absolute;left:152px;top:46px;width:896px;height:808px;
    overflow:hidden;background:var(--wash-white);
    box-shadow:0 10px 30px rgba(60,20,70,.12);
  }
  .label__top-band{position:absolute;left:0;top:0;width:100%;height:56px;background:var(--band-purple);}
  .label__artwork{
    position:absolute;left:0;top:56px;width:100%;height:640px;
    background:
      radial-gradient(ellipse at 20% 10%, rgba(225,170,220,.55), transparent 45%),
      radial-gradient(ellipse at 85% 15%, rgba(200,170,235,.6), transparent 45%),
      radial-gradient(ellipse at 55% 65%, var(--wash-pink), transparent 60%),
      linear-gradient(180deg, var(--wash-white) 0%, var(--wash-lilac) 45%, #d9a0e3 100%);
  }
  .label__text{position:absolute;left:0;width:100%;text-align:center;line-height:1;}
  .title-organic{top:130px;font:400 84px "Josefin Sans",sans-serif;color:var(--ink-navy);letter-spacing:-1px;}
  .title-collagen{top:222px;font:700 134px "Josefin Sans",sans-serif;color:var(--ink-navy);letter-spacing:1px;}
  .title-powder{top:345px;font:400 98px "Josefin Sans",sans-serif;color:var(--ink-navy);letter-spacing:6px;}
  .subtitle{top:436px;font:400 40px "Josefin Sans",sans-serif;color:var(--ink-dark);letter-spacing:-.5px;}
  .types-pill{
    position:absolute;left:208px;top:494px;width:484px;height:66px;
    border-radius:14px;
    background:linear-gradient(180deg,var(--silver-light) 0%,var(--silver-mid) 55%,var(--silver-dark) 100%);
    border-bottom:6px solid var(--band-purple);
    display:flex;align-items:center;justify-content:center;
    font:600 37px "Fira Sans Condensed",sans-serif;color:var(--ink-dark);letter-spacing:.5px;
  }
  .benefits{top:592px;font:500 26px "Fira Sans Condensed",sans-serif;color:var(--ink-dark);}
  .benefits strong{font-weight:700;}
  .label__bottom{position:absolute;left:0;top:0;width:896px;height:808px;}
  .flavor{top:649px;font:700 42px "Fira Sans Condensed",sans-serif;color:var(--ink-dark);letter-spacing:1px;}
  .band-text{position:absolute;color:var(--white);font-family:"Fira Sans Condensed",sans-serif;font-weight:600;line-height:1.1;text-align:center;}
  .servings{left:124px;top:714px;width:160px;font-size:32px;}
  .net-weight{left:640px;top:696px;width:160px;font-size:28px;}
  .supplement-type{left:298px;top:764px;width:300px;font-size:22px;font-weight:700;}
</style>
</head>
<body>
  <div class="label">
    <div class="label__top-band"></div>
    <div class="label__artwork" role="img" aria-label="Soft watercolour wash in lilac and pink with drifting leafy branches and sparkles"></div>

    <svg class="label__bottom" viewBox="0 0 896 808" aria-hidden="true">
      <defs>
        <linearGradient id="silverEdge" x1="0" y1="0" x2="0" y2="1">
          <stop offset="0" stop-color="#f4f6f8"/>
          <stop offset="1" stop-color="#9aa1ab"/>
        </linearGradient>
      </defs>
      <path d="M0 671 H270 C280 671 280 710 300 710 H611 C631 710 631 671 641 671 H896 V808 H0 Z" fill="url(#silverEdge)"/>
      <path d="M0 677 H266 C276 677 278 716 300 716 H611 C633 716 635 677 645 677 H896 V808 H0 Z" fill="var(--band-purple)"/>
      <path d="M0 790 H896 V808 H0 Z" fill="var(--band-purple-dark)"/>
    </svg>

    <p class="label__text title-organic">ORGANIC</p>
    <p class="label__text title-collagen">COLLAGEN</p>
    <p class="label__text title-powder">POWDER</p>
    <p class="label__text subtitle">ELASTIN + HYALURONIC ACID</p>
    <div class="types-pill">COLLAGEN TYPES I, II &amp; III</div>
    <p class="label__text benefits">Supports Beautiful <strong>SKIN, HAIR, &amp; NAILS</strong></p>
    <p class="label__text flavor">FLAVOR</p>

    <p class="band-text servings">30 Servings</p>
    <p class="band-text supplement-type">DIETARY SUPPLEMENT</p>
    <p class="band-text net-weight">Net Wt<br>908g (32oz)</p>
  </div>
</body>
</html>
```